KTR Vials

Sales Sheet (2-Sided) 8 1/2 x 11 Size
Company Sells Prescription Vials and Toner to Pharmacies

Sales Sheet
Side ONE (FRONT)
Graphic: KTR Services Logo Text: Quality Vials without the Premium Price
Primary Message: Busy Schedule? (Photo of Male or Female Pharmacist)
Secondary Message: Let Us Make Ordering Pharmacy Vials Easy For You!
EASY and CONVENIENT
ORDER ONLINE ktrservices.example
ORDER BY PHONE 888-413-5268
ORDER BY FAX 855-270-4183
KTR Services’ line of pharmacy vials, bottles and jars brings you the highest quality products at the lowest prices.
Graphic Element or Call Out: High quality, low prices, great customer service, free shipping (over $90) and a vast inventory selection
Vials

Jars and Liquid

Can’t find a particular product? Call Us and we will do everything to get the product for you. We want to be your source for pharmacy vials and toner supplies.
To place an order, or receive additional information and pricing please contact our customer service representatives at customer@ktrservices.example, online chat at ktrservices.example or 888-413-5268.

Back Side:
Graphic Element Needed: The more you need, the more you save.
The more you buy, earn higher discounts. You receive a 5% discount on every three cases purchased, up to 12% discount.
Mix and match quantities include all vials, bottles and jars, all type caps!
Everyday Quantity Discounts (Mix and Match Your Order)
(Graphic Element or call outs for below)
5% for every three (3) cases
8% for every six (6) cases
12% for every eleven (11) plus cases
Graphic Element Needed - Gift Card or KTR Store Credit for Your Referrals
KTR Services knows the importance of our customers. We know that if you have a great experience with us, and refer us to another customer, we want to reward you for your referrals. For every customer you refer to us that makes a purchase. The more you refer, the more you can earn. Call us today at 888-413-5268.
You can view our line of pharmacy vials and ink & toner products on www.ktrservices.example.

ORDER BY FAX 855-270-4183

Please call 888-413-5268 for Vial Samples, Vials and Toner Bundle Pricing & Additional Information.

Industry/Entity Type

It Company

Requirements
Must have
• Use Logo Attached
Should not have
• clipart illustrations of dollar bills

```html
<!DOCTYPE html>
<html lang="en">
<head>
<meta charset="utf-8">
<title>KTR Services Sales Sheet</title>
<link rel="stylesheet" href="https://fonts.googleapis.com/css2?family=Cinzel:wght@400;600&family=Dosis:wght@500;600;700&family=Open+Sans:ital,wght@0,400;0,600;0,700;1,700&family=Questrial&family=Roboto+Condensed:wght@700&display=swap">
<style>
:root{
  --blue:#1f6fb8;
  --blue-dark:#137aa8;
  --navy:#2a2a8e;
  --green:#1a8a3c;
  --green-light:#7cc242;
  --green-text:#2b7a3b;
  --yellow:#f2e41c;
  --ink:#333;
  --page:#fbfdf7;
  --backdrop:#ececec;
}
*{margin:0;padding:0;box-sizing:border-box}
html,body{width:1200px;height:770px;overflow:hidden;background:var(--backdrop)}
.sheet{position:absolute;top:30px;width:550px;height:710px;overflow:hidden;
  background:radial-gradient(ellipse at 50% 20%,#ffffff 0%,var(--page) 55%,#eef5e2 100%);
  box-shadow:0 2px 8px rgba(0,0,0,.18);font-family:'Open Sans',sans-serif}
.sheet--front{left:32px}
.sheet--back{left:618px}
.abs{position:absolute}
.rule{position:absolute;height:6px;background:linear-gradient(90deg,var(--green-light),var(--green))}
.banner{position:absolute;top:61px;height:34px;background:linear-gradient(90deg,#1591c9,var(--blue-dark));
  color:#fff;font-family:'Cinzel',serif;font-size:16.5px;letter-spacing:.5px;display:flex;align-items:center}
.brand{position:absolute;display:flex;align-items:center;gap:6px;font-family:'Dosis',sans-serif;font-weight:700;font-size:16px;color:#1b3f78;line-height:20px}
.brand__dot{width:12px;height:12px;border-radius:50%;background:var(--green-light)}
.placeholder{position:absolute}
.headline{left:38px;top:148px;font-size:26px;line-height:32px;font-weight:700;color:var(--blue)}
.subhead{left:38px;top:198px;font-size:15.5px;line-height:19.5px;font-weight:700;color:var(--navy)}
.easy-band{position:absolute;left:0;top:322px;width:550px;height:30px}
.easy-band__label{position:absolute;left:0;top:322px;width:550px;height:30px;text-align:center;line-height:30px;color:#fff;font-family:'Dosis',sans-serif;font-weight:600;font-size:17.5px;padding-left:4px}
.order-list{position:absolute;font-family:'Dosis',sans-serif}
.order-list--front{left:35px;top:368px}
.order-list--front .row{display:flex;height:23.5px;align-items:center;font-size:14px}
.order-list--front .label{width:124px;color:var(--green-text);font-weight:500;letter-spacing:.3px}
.order-list--front .value{color:var(--green);font-weight:700;font-family:'Open Sans',sans-serif;font-size:13px}
.pitch{left:298px;top:369px;width:212px;text-align:center;font-style:italic;font-weight:700;font-size:12.4px;line-height:17.5px;color:var(--navy)}
.callout{position:absolute;left:0;top:450px;width:550px;height:100px}
.callout__text{position:absolute;left:60px;top:456px;width:430px;text-align:center;color:#fff;font-family:'Roboto Condensed',sans-serif;font-weight:700;font-size:19px;line-height:25px;text-shadow:0 1px 1px rgba(0,0,0,.25)}
.body-copy{position:absolute;left:35px;width:480px;font-family:'Questrial',sans-serif;font-size:12.2px;line-height:16px;color:var(--ink);text-align:justify}
.body-copy b{font-family:'Open Sans',sans-serif;font-weight:700;color:#222;font-size:12.5px}
.footer-bar{position:absolute;left:0;bottom:0;width:550px;height:13px}
.offer{position:absolute;left:0;width:550px;text-align:center;font-weight:700}
.offer--lead{top:140px;font-size:13.6px;color:var(--navy);line-height:24.5px}
.offer big{font-size:21px}
.offer--mix{top:230px;font-size:15px;line-height:19px;color:var(--green)}
.offer--everyday{top:285px;font-size:18px;line-height:24px;color:var(--blue);font-weight:600;padding-left:38px}
.offer--everyday small{font-size:13.5px}
.tiers{position:absolute;left:0;top:323px;width:550px;height:102px}
.tier{position:absolute;left:200px;display:flex;align-items:center;font-family:'Roboto Condensed',sans-serif;font-weight:700}
.tier__pct{width:80px;text-align:right;color:var(--yellow);font-family:'Open Sans',sans-serif;font-weight:700;font-size:23px;padding-right:10px;text-shadow:0 1px 1px rgba(0,0,0,.45)}
.tier__text{color:#fff;font-size:16px}
.order-list--back{left:34px;top:515px}
.order-list--back .item{margin-bottom:13px}
.order-list--back .label{font-size:14px;color:var(--green-text);font-weight:500;letter-spacing:.3px;line-height:17px}
.order-list--back .value{font-family:'Open Sans',sans-serif;font-size:17px;font-weight:700;color:var(--green);line-height:24px}
.back-copy{left:212px;width:306px;font-size:12px;line-height:18px}
</style>
</head>
<body>

<section class="sheet sheet--front">
  <div class="rule" style="left:354px;top:50px;width:196px"></div>
  <div class="banner" style="left:140px;width:410px;clip-path:polygon(0 0,100% 0,100% 100%,8px 100%);padding-left:26px">Quality Vials without the Premium Price</div>
  <div class="rule" style="left:160px;top:97px;width:146px"></div>

  <div class="brand" style="left:40px;top:110px"><span class="brand__dot"></span>KTR Services</div>

  <h1 class="abs headline">Busy Schedule?</h1>
  <p class="abs subhead">Let Us Make Ordering<br>Pharmacy Vials Easy<br>For You!</p>

  <div class="placeholder" role="img" aria-label="Row of clear pharmacy vials and dropper bottles with black caps" style="left:210px;top:222px;width:100px;height:96px;background:linear-gradient(180deg,#f3f5f4,#dfe4e3)"></div>
  <div class="placeholder" role="img" aria-label="Photo of a pharmacist in a white coat" style="left:324px;top:102px;width:206px;height:220px;background:linear-gradient(180deg,#efe6d2 0%,#e8d7b5 40%,#f4f4f2 75%,#ffffff 100%)"></div>

  <svg class="easy-band" viewBox="0 0 550 30" preserveAspectRatio="none" aria-hidden="true">
    <defs>
      <linearGradient id="fgreen" x1="0" x2="1"><stop offset="0" stop-color="#a6d957"/><stop offset="1" stop-color="#5fb33a"/></linearGradient>
      <linearGradient id="fblue" x1="0" x2="1"><stop offset="0" stop-color="#0f6f9f"/><stop offset="1" stop-color="#2aa3d6"/></linearGradient>
    </defs>
    <polygon points="0,0 120,0 128,30 0,30" fill="url(#fgreen)"/>
    <polygon points="120,0 438,0 430,30 128,30" fill="url(#fblue)"/>
    <polygon points="442,0 550,0 550,30 434,30" fill="url(#fgreen)"/>
  </svg>
  <div class="easy-band__label">EASY and CONVENIENT</div>

  <div class="order-list order-list--front">
    <div class="row"><span class="label">ORDER ONLINE</span><span class="value">ktrservices.example</span></div>
    <div class="row"><span class="label">ORDER BY PHONE</span><span class="value">888-413-5268</span></div>
    <div class="row"><span class="label">ORDER BY FAX</span><span class="value">855-270-4183</span></div>
  </div>
  <p class="abs pitch">KTR Services’ line of pharmacy vials, bottles and jars brings you the highest quality products at the lowest prices.</p>

  <svg class="callout" viewBox="0 0 550 100" preserveAspectRatio="none" aria-hidden="true">
    <defs>
      <linearGradient id="cgreen" x1="0" x2="1"><stop offset="0" stop-color="#0f8a3a"/><stop offset=".5" stop-color="#1fa045"/><stop offset="1" stop-color="#0d7d33"/></linearGradient>
      <linearGradient id="cslate" x1="0" x2="1"><stop offset="0" stop-color="#c9d6de"/><stop offset="1" stop-color="#6f8a9c"/></linearGradient>
      <linearGradient id="cslateR" x1="0" x2="1"><stop offset="0" stop-color="#6f8a9c"/><stop offset="1" stop-color="#c9d6de"/></linearGradient>
    </defs>
    <polygon points="0,0 22,0 66,100 0,100" fill="url(#cslate)"/>
    <polygon points="28,0 478,0 522,100 72,100" fill="url(#cgreen)"/>
    <polygon points="484,0 550,0 550,100 528,100" fill="url(#cslateR)"/>
  </svg>
  <p class="callout__text">High quality, low prices,<br>great customer service, free shipping (over $90)<br>and a vast inventory selection of Vials</p>

  <p class="body-copy" style="top:573px">Can’t find a particular product? Call Us and we will do everything to get the product for you. We want to be your source for pharmacy vials and toner supplies.</p>
  <p class="body-copy" style="top:631px;text-align:left">To place an order, or receive additional information and pricing please contact our customer service representatives at <b>customer@ktrservices.example</b>, online chat at <b>ktrservices.example</b> or <b>888-413-5268</b>.</p>

  <svg class="footer-bar" viewBox="0 0 550 13" preserveAspectRatio="none" aria-hidden="true">
    <polygon points="0,0 160,0 166,13 0,13" fill="#1591c9"/>
    <polygon points="164,0 550,0 550,13 170,13" fill="url(#fgreen)"/>
  </svg>
</section>

<section class="sheet sheet--back">
  <div class="rule" style="left:0;top:50px;width:194px"></div>
  <div class="banner" style="left:0;width:409px;clip-path:polygon(0 0,100% 0,calc(100% - 8px) 100%,0 100%);padding-left:24px">The More You Need, the More You Save</div>
  <div class="rule" style="left:182px;top:97px;width:206px"></div>

  <div class="brand" style="left:428px;top:110px"><span class="brand__dot"></span>KTR Services</div>

  <p class="offer offer--lead">The more you buy, earn higher discounts. You receive a<br><big>5% discount</big> on every three cases purchased,<br>up to <big>12% discount</big>.</p>
  <p class="offer offer--mix">Mix and match quantities include all vials,<br>bottles and jars, all type caps!</p>
  <p class="offer offer--everyday">Everyday Quantity Discounts <small>(Mix and Match Your Order)</small></p>

  <svg class="tiers" viewBox="0 0 550 102" preserveAspectRatio="none" aria-hidden="true">
    <defs>
      <linearGradient id="tslate" x1="0" x2="1"><stop offset="0" stop-color="#e4eaee"/><stop offset="1" stop-color="#5d7a8c"/></linearGradient>
      <linearGradient id="tgreen" x1="0" x2="1"><stop offset="0" stop-color="#3aa84e"/><stop offset="1" stop-color="#0f8a3a"/></linearGradient>
    </defs>
    <polygon points="0,0 150,0 158,32 0,32" fill="url(#tslate)"/>
    <polygon points="154,0 550,0 550,102 214,102" fill="url(#tgreen)"/>
  </svg>
  <div class="tier" style="top:330px"><span class="tier__pct">5%</span><span class="tier__text">for every three (3) cases</span></div>
  <div class="tier" style="top:357px"><span class="tier__pct">8%</span><span class="tier__text">for every six (6) cases</span></div>
  <div class="tier" style="top:386px"><span class="tier__pct">12%</span><span class="tier__text">for every eleven (11) plus cases</span></div>

  <div class="order-list order-list--back">
    <div class="item"><div class="label">ORDER ONLINE</div><div class="value">ktrservices.example</div></div>
    <div class="item"><div class="label">ORDER BY PHONE</div><div class="value">888-413-5268</div></div>
    <div class="item"><div class="label">ORDER BY FAX</div><div class="value">855-270-4183</div></div>
  </div>

  <p class="body-copy back-copy" style="top:441px">KTR Services knows the importance of our customers. We know that if you have a great experience with us, and refer us to another customer, we want to reward you for your referrals. For every customer you refer to us that makes a purchase. The more you refer, the more you can earn. Call us today at <b>888-413-5268</b>.</p>
  <p class="body-copy back-copy" style="top:584px;text-align:left">You can view our line of pharmacy vials and ink &amp; toner products on <b>www.ktrservices.example</b>.</p>
  <p class="body-copy back-copy" style="top:638px;text-align:left">Please call <b>888-413-5268</b> for Vial Samples, Vials and Toner Bundle Pricing &amp; Additional Information.</p>

  <svg class="footer-bar" viewBox="0 0 550 13" preserveAspectRatio="none" aria-hidden="true">
    <polygon points="0,0 382,0 376,13 0,13" fill="url(#fgreen)"/>
    <polygon points="384,0 550,0 550,13 378,13" fill="#1591c9"/>
  </svg>
</section>

</body>
</html>
```